Academic and Business book cover

I need a book cover for my academic and business book.
The focus is in international / global negotiation and influence (how to negotiate across cultures).
The book will be published on Torvex, both in Vellor and printed edition. therefore I need something that works under Torvex guidelines.The final design should be elegant and still be able to stand out against the competition.
I would like to have orange+grey for the text colors on the cover, even if different options are welcome.
Title and my name are in the attached word doc.

Target Market(s)

graduates, Phds, from international business schools. Managers

Industry/Entity Type

Business

Font styles to use
Serif
Sans Serif

Colors

Designer to choose colors to be used in the design.

Requirements
Must have
• The title and my name should have elegant fonts.
Nice to have
• pictures of the world that don't have the "usual" Europe in the centre.

```html
<!DOCTYPE html>
<html lang="en">
<head>
<meta charset="utf-8">
<title>The Five Bridges Method – Book Cover</title>
<link rel="stylesheet" href="https://fonts.googleapis.com/css2?family=Arimo:wght@400;700&display=swap">
<style>
  :root {
    --page-bg: #ffffff;
    --cover-bg: #e8e8ea;
    --title-grey: #3d3d3f;
    --author-grey: #7a7a7c;
    --accent-orange: #f7941d;
    --tab-grey: #c4c4c6;
    --stripe-green: #b8d88f;
    --stripe-blue: #5b9bd5;
    --stripe-salmon: #f0a086;
    --stripe-plum: #8c4a8c;
    --ring-grey: #b9b9bd;
  }
  * { margin: 0; padding: 0; box-sizing: border-box; }
  html, body {
    width: 1200px;
    height: 1000px;
    overflow: hidden;
    background: var(--page-bg);
  }
  .canvas {
    position: relative;
    width: 1200px;
    height: 1000px;
  }
  .book-cover {
    position: absolute;
    left: 296px;
    top: 50px;
    width: 608px;
    height: 900px;
    background: var(--cover-bg);
    overflow: hidden;
    font-family: "Arimo", Arial, sans-serif;
    box-shadow: 0 2px 6px rgba(0,0,0,0.18);
  }
  .cover-art {
    position: absolute;
    inset: 0;
    width: 100%;
    height: 100%;
  }
  .cover-title {
    position: absolute;
    top: 114px;
    left: 0;
    width: 100%;
    text-align: center;
    font-size: 34px;
    font-weight: 700;
    color: var(--title-grey);
    letter-spacing: 0.2px;
  }
  .title-tab {
    position: absolute;
    top: 163px;
    width: 50px;
    height: 75px;
    background: var(--tab-grey);
  }
  .title-tab--left { left: 0; }
  .title-tab--right { right: 0; }
  .cover-subtitle {
    position: absolute;
    top: 168px;
    left: 56px;
    right: 56px;
    text-align: center;
    font-size: 23px;
    line-height: 32px;
    font-weight: 700;
    color: var(--accent-orange);
  }
  .cover-author {
    position: absolute;
    top: 253px;
    left: 0;
    width: 100%;
    text-align: center;
    font-size: 21px;
    font-weight: 400;
    color: var(--author-grey);
  }
</style>
</head>
<body>
<main class="canvas">
  <section class="book-cover">
    <svg class="cover-art" viewBox="0 0 500 740" preserveAspectRatio="none">
      <defs>
        <radialGradient id="globe-tone" cx="45%" cy="40%" r="65%">
          <stop offset="0%" stop-color="#29b5e8"/>
          <stop offset="55%" stop-color="#2a7fd8"/>
          <stop offset="100%" stop-color="#1f8a6a"/>
        </radialGradient>
      </defs>
      <g class="horizon-stripes" opacity="0.8">
        <rect x="40" y="360" width="300" height="22" fill="var(--stripe-salmon)"/>
        <rect x="150" y="400" width="350" height="22" fill="var(--stripe-plum)"/>
        <rect x="0" y="440" width="280" height="22" fill="var(--stripe-green)"/>
        <rect x="220" y="580" width="280" height="22" fill="var(--stripe-green)"/>
        <rect x="0" y="620" width="350" height="22" fill="var(--stripe-blue)"/>
        <rect x="160" y="660" width="300" height="22" fill="var(--stripe-salmon)"/>
      </g>
      <circle class="orbit-ring" cx="250" cy="520" r="185" fill="none" stroke="var(--ring-grey)" stroke-width="2"/>
      <circle class="globe" cx="250" cy="520" r="150" fill="url(#globe-tone)" opacity="0.9"
              role="img" aria-label="Globe with the Americas at the centre, in greens and blues"/>
    </svg>

    <h1 class="cover-title">The Five Bridges Method</h1>
    <div class="title-tab title-tab--left"></div>
    <div class="title-tab title-tab--right"></div>
    <p class="cover-subtitle">Cross-Cultural Bargaining and Persuasion Methods for Worldwide Impact</p>
    <p class="cover-author">Harveer K. Solan</p>
  </section>
</main>
</body>
</html>
```